Need Bold, Hip Card for Concert Ticket Website Gleaming Passes!

Hi there! I am putting together a business/website that sells event tickets (mostly concerts, but also some sports and theater). Think SeatNook, but much smaller. The site is called Gleaming Passes. I have a new logo (attached, with black/red/white color scheme), and am looking for a modern/cool/original business card design. Note that I am thinking of having the card itself in the shape of a ticket (die cut), so you may want to keep that in mind when designing, but I'm not set on that. I'm also open to alternative card sizes, thicknesses, glossy, spot UV, etc. in order to stand out. I'm attaching a potential die cut template and a sample card using that template in case you want to work with that.
Target Market(s)
Music fans, people that like going to see live events
Industry/Entity Type
Entertainment
Contact Information for Business Card
Information that I'd like to have:
website address - www.gleamingpasses.example
phone number: 1-833-5GLEAMNG (532-6264)
my name - Wendel Pike

```html
<!DOCTYPE html>
<html lang="en">
<head>
<meta charset="utf-8">
<title>Gleaming Passes – Business Card Presentation</title>
<link href="https://fonts.googleapis.com/css2?family=Lato:wght@300;400;700&family=Montserrat:wght@700;800&display=swap" rel="stylesheet">
<style>
  :root {
    --board: #e5e5e5;
    --ink: #111111;
    --red: #ec2028;
    --night: #1b1b1e;
    --paper: #fbfbfb;
    --text-grey: #2b2b2b;
    --shadow: 6px 10px 10px rgba(0,0,0,0.35);
  }
  * { margin: 0; padding: 0; box-sizing: border-box; }
  html, body { width: 1200px; height: 960px; overflow: hidden; }
  body {
    background: var(--board);
    position: relative;
    font-family: "Lato", Arial, sans-serif;
    color: var(--ink);
  }
  .side-label {
    position: absolute;
    font-family: "Montserrat", Arial, sans-serif;
    font-weight: 700;
    font-size: 26px;
    letter-spacing: 0.42em;
    transform: translate(-50%, -50%);
    white-space: nowrap;
    padding-left: 0.42em;
  }
  .divider {
    position: absolute; left: 124px; top: 438px;
    width: 950px; height: 6px; background: var(--ink);
    box-shadow: 4px 6px 6px rgba(0,0,0,0.3);
  }
  .card { position: absolute; box-shadow: var(--shadow); overflow: hidden; }

  .brand-name {
    font-family: "Montserrat", Arial, sans-serif;
    font-weight: 800;
    text-transform: uppercase;
    line-height: 0.95;
    display: flex; align-items: center; gap: 10px;
    position: absolute; left: 50%; transform: translateX(-50%);
    white-space: nowrap;
    z-index: 2;
  }
  .brand-mark { display: block; flex: none; }

  /* Front */
  .card-front { left: 307px; top: 58px; width: 587px; height: 352px; background: #fff; }
  .hero {
    position: absolute; left: 0; top: 0; width: 100%; height: 176px;
    background:
      repeating-linear-gradient(90deg, rgba(255,255,255,0.04) 0 1px, transparent 1px 3px),
      radial-gradient(ellipse at 50% 30%, #4a4a4f 0%, var(--night) 70%);
  }
  .front-art { position: absolute; left: 0; top: 0; }
  .front-brand { top: 72px; color: #fff; font-size: 30px; gap: 12px; }
  .front-brand .brand-mark { width: 38px; height: 38px; background: var(--red); }
  .address {
    position: absolute; top: 190px; left: 0; width: 100%; text-align: center;
    color: #fff; font-weight: 700; font-size: 12.5px;
  }
  .person { position: absolute; right: 337px; top: 244px; text-align: right; }
  .person-name { font-weight: 400; font-size: 20px; color: var(--text-grey); line-height: 1.1; }
  .person-role { font-size: 11.5px; color: var(--red); margin-top: 2px; }
  .contacts { position: absolute; left: 347px; top: 232px; list-style: none; }
  .contacts li {
    display: flex; align-items: center; gap: 10px; height: 23px;
    font-size: 11px; color: var(--text-grey);
  }
  .contacts svg { width: 17px; height: 17px; flex: none; }
  .front-url {
    position: absolute; top: 327px; left: 0; width: 100%; text-align: center;
    color: #ffd7d9; font-weight: 300; font-size: 10px; letter-spacing: 0.45em;
  }

  /* Backs */
  .card-back { width: 360px; height: 215px; }
  .card-back .brand-name { top: 86px; font-size: 19px; }
  .card-back .brand-mark { width: 24px; height: 24px; }
  .back-url {
    position: absolute; left: 0; width: 100%; top: 184px; text-align: center;
    font-weight: 700; font-size: 7px; letter-spacing: 0.35em;
  }
  .back-white { left: 419px; top: 464px; height: 217px; background: var(--paper); }
  .back-white .brand-name { color: var(--red); top: 80px; }
  .back-white .brand-mark { background: var(--ink); }
  .back-white .back-url { color: var(--ink); top: 186px; }
  .back-black { left: 59px; top: 710px; background: #000; }
  .back-black .brand-name, .back-black .back-url { color: #fff; }
  .back-black .brand-mark { background: var(--red); }
  .back-red { left: 781px; top: 710px; background: var(--red); box-shadow: 6px 10px 12px rgba(236,32,40,0.45); }
  .back-red .brand-name, .back-red .back-url { color: #fff; }
  .back-red .brand-mark { background: #fff; }
</style>
</head>
<body>
  <div class="side-label" style="left:600px;top:34px">FRONT</div>

  <section class="card card-front">
    <div class="hero" role="img" aria-label="Dark photo of a concert crowd with raised hands under stage lights"></div>
    <svg class="front-art" width="587" height="352" viewBox="0 0 587 352" aria-hidden="true">
      <rect x="0" y="176" width="587" height="5" fill="#ec2028"/>
      <polygon points="137,176 449,176 421,212 165,212" fill="#ec2028"/>
      <rect x="0" y="347" width="587" height="5" fill="#ec2028"/>
      <polygon points="165,315 421,315 449,352 137,352" fill="#ec2028"/>
      <rect x="292" y="234" width="2" height="62" fill="#ec2028"/>
    </svg>
    <div class="brand-name front-brand"><span class="brand-mark"></span><span>Gleaming<br>Passes</span></div>
    <div class="address">Your Company Address 9912-B</div>
    <div class="person">
      <div class="person-name">Wendel Pike</div>
      <div class="person-role">Entertainment</div>
    </div>
    <ul class="contacts">
      <li>
        <svg viewBox="0 0 20 20"><circle cx="10" cy="10" r="10" fill="#ec2028"/><path d="M5 8.5c0-1.5 2.5-2.5 5-2.5s5 1 5 2.5v1h-2.5v-1.3h-5v1.3H5z M6.5 14l1.5-4h4l1.5 4z" fill="#fff"/></svg>
        1-833-5GLEAMNG (532-6264)
      </li>
      <li>
        <svg viewBox="0 0 20 20"><circle cx="10" cy="10" r="10" fill="#ec2028"/><rect x="5" y="6.5" width="10" height="7" fill="none" stroke="#fff" stroke-width="1.2"/><path d="M5 6.5l5 4 5-4" fill="none" stroke="#fff" stroke-width="1.2"/></svg>
        gleamingpasses@email.example
      </li>
      <li>
        <svg viewBox="0 0 20 20"><circle cx="10" cy="10" r="10" fill="#ec2028"/><rect x="5" y="5.5" width="10" height="7" fill="none" stroke="#fff" stroke-width="1.4"/><rect x="7" y="13.5" width="6" height="1.3" fill="#fff"/></svg>
        www.gleamingpasses.example
      </li>
    </ul>
    <div class="front-url">www.gleamingpasses.example</div>
  </section>

  <div class="divider"></div>

  <div class="side-label" style="left:253px;top:578px">BACK</div>
  <div class="side-label" style="left:950px;top:578px">BACK</div>
  <div class="side-label" style="left:600px;top:838px">BACK</div>

  <section class="card card-back back-white">
    <div class="brand-name"><span class="brand-mark"></span><span>Gleaming<br>Passes</span></div>
    <div class="back-url">www.gleamingpasses.example</div>
  </section>

  <section class="card card-back back-black">
    <div class="brand-name"><span class="brand-mark"></span><span>Gleaming<br>Passes</span></div>
    <div class="back-url">www.gleamingpasses.example</div>
  </section>

  <section class="card card-back back-red">
    <div class="brand-name"><span class="brand-mark"></span><span>Gleaming<br>Passes</span></div>
    <div class="back-url">www.gleamingpasses.example</div>
  </section>
</body>
</html>
```